Business Card Design for Fashion Tech Startup

Dear designers, we need a business card for Asia's premier fashion tech startup.!

PebbleHop is discovery e-commerce destination for busy, discerning parents in Asia featuring leading independent designers of baby, kids fashion apparel and sustainable brands from around the world.

PebbleHop is a modern, contemporary fashion tech startup targeting well-educated, well travelled and affluent parents. We're NOT your typical kiddy store!! Our design philosophy & e-commerce site is more like Vask.com, Orimesa.com, Pondwick.com, Farthollow.com.
Updates

Hi, size of the business card should be 84mm X 55mm. Would appreciate some business card layouts in Portrait as added consideration, i fancy the idea of a Portrait business card. What's important is that the business card should pique the receiver's interest to log onto the website to learn more. Many thanks and love forward to the designs!

Target Market(s)

Though modern, classy in look, feel & positioning, PebbleHop does possess a cheeky, fun-loving personality as depicted by its logo and the segment it targets (baby, kids) though the key decision makers i.e primarily mums between 25-40 who are well educated/travelled, local & expatriates, internet/digitally savvy, mid-high income working mums.

Industry/Entity Type

E-Commerce

Requirements
Must have
• Name, designation, email, phone & mobile number.
Company url : www.pebblehop.sg
Slogan : Curated online finds for thoughtful, on-the-go families
Nice to have
• Call to Action such as a Discount code offering 10% discount
or asking people to "Like" us on our Chatterly page/Chatterly URL

```html
<!DOCTYPE html>
<html lang="en">
<head>
<meta charset="utf-8">
<title>PebbleHop Business Card</title>
<link rel="stylesheet" href="https://fonts.googleapis.com/css2?family=Mulish:wght@400;700;800&display=swap">
<style>
  :root {
    --coral: #ec7a62;
    --navy: #2f5270;
    --paper: #fbfbf9;
    --backdrop: #e8e7e4;
    --ink-muted: #4a6a85;
  }
  * { box-sizing: border-box; margin: 0; padding: 0; }
  html, body { width: 1200px; height: 900px; overflow: hidden; }
  body {
    background: var(--backdrop);
    font-family: "Mulish", "Century Gothic", sans-serif;
    position: relative;
  }
  .card {
    position: absolute;
    width: 504px;
    height: 330px;
    background: var(--paper);
    box-shadow: 0 10px 28px rgba(0,0,0,0.10);
    overflow: hidden;
  }
  .card--front { left: 64px; top: 130px; }
  .card--back { left: 632px; top: 440px; }

  .pattern-field {
    position: absolute;
    inset: 0;
    background: linear-gradient(135deg, #f7d3c8 0%, #f6efec 45%, #d3dce5 100%);
  }
  .front-mark {
    position: absolute;
    left: 50%; top: 50%;
    transform: translate(-50%, -50%);
    display: flex;
    align-items: center;
    gap: 14px;
    white-space: nowrap;
  }
  .front-mark__dot {
    width: 44px; height: 44px;
    border-radius: 50%;
    background: var(--navy);
    flex: none;
  }
  .front-mark__name {
    font-weight: 800;
    font-size: 40px;
    color: var(--coral);
    letter-spacing: -0.5px;
  }

  .brand {
    position: absolute;
    right: 44px; top: 58px;
    display: flex;
    align-items: center;
    gap: 8px;
  }
  .brand__dot {
    width: 26px; height: 26px;
    border-radius: 50%;
    background: var(--navy);
  }
  .brand__name {
    font-weight: 800;
    font-size: 20px;
    color: var(--coral);
  }
  .slogan {
    position: absolute;
    right: 44px; top: 104px;
    width: 210px;
    text-align: right;
    font-size: 12px;
    line-height: 1.3;
    color: var(--ink-muted);
  }
  .person {
    position: absolute;
    left: 44px; top: 170px;
  }
  .person__name {
    font-weight: 700;
    font-size: 17px;
    color: var(--navy);
  }
  .person__role {
    font-size: 14px;
    color: var(--ink-muted);
    margin-top: 2px;
  }
  .contacts {
    position: absolute;
    left: 44px; top: 236px;
    list-style: none;
  }
  .contacts__item {
    display: flex;
    align-items: center;
    gap: 10px;
    font-size: 14px;
    color: var(--navy);
    line-height: 1.45;
  }
  .contacts__icon { width: 11px; height: 11px; fill: var(--coral); flex: none; }
</style>
</head>
<body>

<section class="card card--front" aria-label="Card front">
  <div class="pattern-field" role="img" aria-label="Playful pattern of coral and navy baby and toy silhouettes"></div>
  <div class="front-mark">
    <span class="front-mark__dot"></span>
    <span class="front-mark__name">PebbleHop.sg</span>
  </div>
</section>

<section class="card card--back" aria-label="Card back">
  <div class="brand">
    <span class="brand__dot"></span>
    <span class="brand__name">PebbleHop</span>
  </div>
  <p class="slogan">Curated online finds for thoughtful, on-the-go families</p>

  <div class="person">
    <p class="person__name">Maren Okafor</p>
    <p class="person__role">managing director</p>
  </div>

  <ul class="contacts">
    <li class="contacts__item">
      <svg class="contacts__icon" viewBox="0 0 12 12" aria-hidden="true"><path d="M2 1h3l1 3-2 1c.7 1.4 1.6 2.3 3 3l1-2 3 1v3c-5.5 0-9-3.5-9-9z"/></svg>
      201.555.0142
    </li>
    <li class="contacts__item">
      <svg class="contacts__icon" viewBox="0 0 12 12" aria-hidden="true"><path d="M3 0h6v12H3zM4 1.5v7.5h4V1.5z"/></svg>
      201.555.0178
    </li>
    <li class="contacts__item">
      <svg class="contacts__icon" viewBox="0 0 12 12" aria-hidden="true"><path d="M0 2h12v8H0zM1 3l5 3.5L11 3z"/></svg>
      maren@pebblehop.sg
    </li>
  </ul>
</section>

</body>
</html>
```